Copper Lantern General Contracting Business Card

My company is a General Contracting and Handyman service based in a private community in Northeast Pennsylvania.
Our cliental is a mix of year round and seasonal homeowners
We pride ourselves i using new and innovative building techniques and always try to build with pride and integrity
Please check my website f(under construction) or a list of services and more information
The files below are my logo and my facebook business page profile pic

Industry/Entity Type

Building

Contact Information for Business Card

Copper Lantern General Contracting
Dale Hurst
Cedar Hollow, Pennsylvania
570-555-0147
dale@cprlantern.com
www.cprlantern.com
www.facebook.com/copperlanterncontracting

```html
<!DOCTYPE html>
<html lang="en">
<head>
<meta charset="utf-8">
<title>Copper Lantern General Contracting – Business Card</title>
<link rel="stylesheet" href="https://fonts.googleapis.com/css2?family=Open+Sans:wght@300;400;600;700;800&display=swap">
<style>
  :root {
    --backdrop: #3a3a3c;
    --card-black: #1b1b1c;
    --card-white: #f1f1f1;
    --accent-red: #d8332b;
    --ink-dark: #1e1e1e;
    --ink-light: #f4f4f4;
  }
  * { box-sizing: border-box; margin: 0; padding: 0; }
  html, body { width: 1200px; height: 819px; overflow: hidden; }
  body {
    background: var(--backdrop);
    font-family: "Open Sans", Arial, sans-serif;
    position: relative;
  }
  .card {
    position: absolute;
    top: 260px;
    width: 520px;
    height: 300px;
    border-radius: 6px;
    overflow: hidden;
    box-shadow: 0 10px 30px rgba(0,0,0,.35);
  }
  .card--front { left: 50px; background: var(--card-black); }
  .card--back { left: 630px; background: var(--card-white); }

  .wordmark {
    display: flex;
    align-items: center;
    gap: 12px;
  }
  .wordmark__square {
    width: 26px; height: 26px;
    background: var(--accent-red);
    flex: none;
  }
  .wordmark__name {
    font-weight: 800;
    text-transform: uppercase;
    line-height: 1.05;
    letter-spacing: .5px;
  }
  .card--front .wordmark {
    position: absolute; left: 0; right: 0; top: 0; bottom: 0;
    justify-content: center;
  }
  .card--front .wordmark__name { color: var(--ink-light); font-size: 30px; }
  .card--front .wordmark__square { width: 34px; height: 34px; }

  .back__top {
    position: absolute; left: 0; right: 0; top: 0; height: 160px;
    display: flex; align-items: center; justify-content: flex-end;
    padding-right: 40px;
  }
  .card--back .wordmark__name { color: var(--ink-dark); font-size: 21px; }

  .back__band {
    position: absolute; left: 0; right: 0; top: 160px; bottom: 0;
    background: var(--card-black);
    border-top: 3px solid var(--accent-red);
  }
  .person-name {
    position: absolute; left: 36px; top: 48px;
    font-size: 28px; color: var(--ink-light);
  }
  .person-name__first { font-weight: 700; }
  .person-name__last { font-weight: 300; }
  .divider {
    position: absolute; left: 250px; top: 18px; bottom: 18px;
    width: 2px; background: var(--accent-red);
  }
  .contact-list {
    position: absolute; left: 268px; top: 20px;
    list-style: none;
  }
  .contact-list li {
    display: flex; align-items: center; gap: 8px;
    color: var(--ink-light);
    font-size: 13px; line-height: 19px;
    white-space: nowrap;
  }
  .contact-list svg { width: 12px; height: 12px; flex: none; fill: var(--accent-red); }
</style>
</head>
<body>

<section class="card card--front" aria-label="Business card front">
  <div class="wordmark">
    <span class="wordmark__square"></span>
    <span class="wordmark__name">Copper Lantern<br>General Contracting</span>
  </div>
</section>

<section class="card card--back" aria-label="Business card back">
  <div class="back__top">
    <div class="wordmark">
      <span class="wordmark__square"></span>
      <span class="wordmark__name">Copper Lantern<br>General Contracting</span>
    </div>
  </div>
  <div class="back__band">
    <p class="person-name"><span class="person-name__first">Dale</span> <span class="person-name__last">Hurst</span></p>
    <span class="divider"></span>
    <ul class="contact-list">
      <li>
        <svg viewBox="0 0 24 24" aria-hidden="true"><path d="M6.6 10.8a15 15 0 0 0 6.6 6.6l2.2-2.2a1 1 0 0 1 1-.25 11.4 11.4 0 0 0 3.6.57 1 1 0 0 1 1 1V20a1 1 0 0 1-1 1A17 17 0 0 1 3 4a1 1 0 0 1 1-1h3.5a1 1 0 0 1 1 1c0 1.25.2 2.45.57 3.57a1 1 0 0 1-.25 1z"/></svg>
        570-555-0147
      </li>
      <li>
        <svg viewBox="0 0 24 24" aria-hidden="true"><path d="M2 5h20v14H2zm2 2v.5l8 5 8-5V7zm0 2.8V17h16V9.8l-8 5z"/></svg>
        dale@cprlantern.com
      </li>
      <li>
        <svg viewBox="0 0 24 24" aria-hidden="true"><path d="M12 2a10 10 0 1 0 0 20 10 10 0 0 0 0-20zm6.9 9h-3a15 15 0 0 0-1.3-5.6A8 8 0 0 1 18.9 11zM12 4.1c.9 1.2 1.8 3.6 1.9 6.9h-3.8c.1-3.3 1-5.7 1.9-6.9zM9.4 5.4A15 15 0 0 0 8.1 11h-3a8 8 0 0 1 4.3-5.6zM5.1 13h3a15 15 0 0 0 1.3 5.6A8 8 0 0 1 5.1 13zm6.9 6.9c-.9-1.2-1.8-3.6-1.900-6.9h3.8c-.1 3.3-1 5.7-1.9 6.9zm2.6-1.3a15 15 0 0 0 1.3-5.6h3a8 8 0 0 1-4.3 5.6z"/></svg>
        www.cprlantern.com
      </li>
      <li>
        <svg viewBox="0 0 24 24" aria-hidden="true"><circle cx="12" cy="12" r="9"/></svg>
        /copperlanterncontracting
      </li>
      <li>
        <svg viewBox="0 0 24 24" aria-hidden="true"><path d="M12 2a7 7 0 0 0-7 7c0 5 7 13 7 13s7-8 7-13a7 7 0 0 0-7-7zm0 9.5A2.5 2.5 0 1 1 12 6.5a2.5 2.5 0 0 1 0 5z"/></svg>
        Cedar Hollow, Pennsylvania
      </li>
    </ul>
  </div>
</section>

</body>
</html>
```